Essential Oil 15ml - package of 6

Design of a box of 6 different essential oils.
+ design of the bottle stickers
My bottles are 15ml clear blue glass.

The pictures attached are my competitors...

Target Market(s)

BRAMBLEWICK USA

Font styles to use
Serif

Requirements
Must have
• Our logo + "essential oil" and type (lavender, eucalyptus etc....)
• 15ml - 0.50 fl.oz.
• special color for the oil type.

```html
<!DOCTYPE html>
<html lang="en">
<head>
<meta charset="utf-8">
<title>Sela Grove Essential Oil Labels</title>
<link rel="stylesheet" href="https://fonts.googleapis.com/css2?family=Bodoni+Moda:wght@400;500&family=Ubuntu:wght@500&display=swap">
<style>
  :root {
    --backdrop: #ececec;
    --label: #3b3b3c;
    --lace: #2a2a2b;
    --lace-soft: #444446;
    --ink-light: #f1f1f1;
    --lemon: #f4cf1e;
    --eucalyptus: #e6262f;
    --lavender: #a22fe6;
  }
  * { margin: 0; padding: 0; box-sizing: border-box; }
  html, body {
    width: 1200px;
    height: 900px;
    overflow: hidden;
    background: var(--backdrop);
  }
  .label-sheet {
    width: 1200px;
    height: 900px;
    display: flex;
    justify-content: center;
    align-items: center;
    gap: 50px;
  }
  .oil-label {
    --accent: var(--lemon);
    position: relative;
    width: 340px;
    height: 440px;
    background: var(--label);
    box-shadow: 0 6px 18px rgba(0,0,0,0.18);
    overflow: hidden;
  }
  .oil-label.lemon { --accent: var(--lemon); }
  .oil-label.eucalyptus { --accent: var(--eucalyptus); }
  .oil-label.lavender { --accent: var(--lavender); }

  .lace-ornament {
    position: absolute;
    left: 10px;
    top: 20px;
    width: 320px;
    height: 400px;
    border-radius: 50%;
    background: radial-gradient(ellipse at center, var(--lace-soft) 0%, var(--lace) 55%, var(--label) 72%);
    opacity: 0.9;
  }
  .brand {
    position: absolute;
    top: 88px;
    left: 0;
    right: 0;
    display: flex;
    justify-content: center;
    align-items: center;
    gap: 10px;
  }
  .brand-dot {
    width: 18px;
    height: 18px;
    border-radius: 50%;
    background: var(--accent);
  }
  .brand-name {
    font-family: "Ubuntu", sans-serif;
    font-weight: 500;
    font-size: 30px;
    color: var(--accent);
    letter-spacing: -0.5px;
  }
  .oil-band {
    position: absolute;
    top: 180px;
    left: 0;
    right: 0;
    height: 62px;
    background: var(--accent);
    display: flex;
    justify-content: center;
    align-items: center;
  }
  .oil-name {
    font-family: "Bodoni Moda", serif;
    font-weight: 500;
    font-size: 40px;
    letter-spacing: 18px;
    margin-right: -18px;
    color: #1c1c1c;
    transform: scaleX(0.82);
  }
  .oil-label.eucalyptus .oil-name,
  .oil-label.lavender .oil-name { color: var(--ink-light); }
  .oil-label.eucalyptus .oil-name { letter-spacing: 12px; margin-right: -12px; }

  .oil-type {
    position: absolute;
    top: 272px;
    left: 0;
    right: 0;
    text-align: center;
    font-family: "Bodoni Moda", serif;
    font-size: 13px;
    letter-spacing: 2px;
    color: var(--ink-light);
  }
  .sprig {
    position: absolute;
    top: 300px;
    left: 150px;
    width: 40px;
    height: 16px;
    border-radius: 8px;
    background: var(--accent);
    opacity: 0.75;
  }
  .volume {
    position: absolute;
    top: 340px;
    left: 0;
    right: 0;
    text-align: center;
    font-family: "Bodoni Moda", serif;
    font-size: 18px;
    color: var(--ink-light);
    transform: scaleX(0.85);
  }
</style>
</head>
<body>
<main class="label-sheet">

  <section class="oil-label lemon">
    <div class="lace-ornament" role="img" aria-label="Dark lace floral ornament framing the label"></div>
    <div class="brand"><span class="brand-dot"></span><span class="brand-name">Sela Grove</span></div>
    <div class="oil-band"><span class="oil-name">lemon</span></div>
    <p class="oil-type">100% ESSENTIAL OIL</p>
    <div class="sprig" role="img" aria-label="Small lemon blossom sprig illustration"></div>
    <p class="volume">15ml - 0.50 fl.oz.</p>
  </section>

  <section class="oil-label eucalyptus">
    <div class="lace-ornament" role="img" aria-label="Dark lace floral ornament framing the label"></div>
    <div class="brand"><span class="brand-dot"></span><span class="brand-name">Sela Grove</span></div>
    <div class="oil-band"><span class="oil-name">eucalyptus</span></div>
    <p class="oil-type">100% ESSENTIAL OIL</p>
    <div class="sprig" role="img" aria-label="Small eucalyptus flower sprig illustration"></div>
    <p class="volume">15ml - 0.50 fl.oz.</p>
  </section>

  <section class="oil-label lavender">
    <div class="lace-ornament" role="img" aria-label="Dark lace floral ornament framing the label"></div>
    <div class="brand"><span class="brand-dot"></span><span class="brand-name">Sela Grove</span></div>
    <div class="oil-band"><span class="oil-name">lavender</span></div>
    <p class="oil-type">100% ESSENTIAL OIL</p>
    <div class="sprig" role="img" aria-label="Small lavender sprig illustration"></div>
    <p class="volume">15ml - 0.50 fl.oz.</p>
  </section>

</main>
</body>
</html>
```